Simple, High-Class Web Design Wanted - Motivational Speakers Site

1. Full Brief/Request & Specs outlined on following video -
http://clipvane-recorder.com/watch/tbWrkLmQyP

2. Use colours, images as you feel suits objective (we are happy to pay up to US$30 for any good images but must have licence/permission).

3. Layout probably similar to existing site - www.podiumvoicehub.com.au / http://podiumvoicehub.com.au/contact.php

4. Must Be Able to Coded for MOBILE-FRIENDLINESS & WordPress friendly Ideal.

5. This is the first, small job of many we/graphic design jobs. If suits, winning designer may be offered all future work direct.

Thanks & look forward to your design. Glen.

Target Market(s)

corporates - high end

Number of Pages Required

2 page

Font styles to use
Sans Serif

Requirements
Must have
• Classy professional look
Nice to have
• all in Video in brief
Should not have
• too many images / new images I haven't approved

```html
<!DOCTYPE html>
<html lang="en">
<head>
<meta charset="utf-8">
<title>Free Industry Services – Find the Speaker for Your Next Event</title>
<link href="https://fonts.googleapis.com/css2?family=Oswald:wght@400;500&family=Open+Sans:wght@400;600;700&display=swap" rel="stylesheet">
<style>
:root{
  --blue:#1a8fdc;
  --blue-dark:#0f6fb3;
  --header:#0d3b2c;
  --green-1:#0e5a2a;
  --green-2:#3aa53a;
  --text:#555c63;
  --muted:#8a9198;
  --note-bg:#e9edf0;
  --foot-bg:#f7f8f9;
  --line:#d5dbe0;
  --white:#ffffff;
}
*{box-sizing:border-box;margin:0;padding:0}
html,body{width:1200px;height:2176px;overflow:hidden;background:var(--white)}
body{font-family:"Open Sans",Arial,sans-serif;color:var(--text);font-size:15px;line-height:1.6}
.wrap{width:1040px;margin:0 auto;position:relative}
.btn{display:inline-block;background:var(--blue);color:var(--white);font-weight:600;text-decoration:none}

.site-header{height:120px;background:var(--header);color:var(--white)}
.site-header .wrap{display:flex;align-items:center;height:100%}
.brand{font-family:"Oswald",sans-serif;font-size:30px;letter-spacing:1px;text-transform:uppercase;white-space:nowrap;flex:1}
.header-contact{display:flex;align-items:center;gap:28px;font-size:15px;white-space:nowrap}
.header-contact span{display:flex;align-items:center;gap:9px}
.header-contact .btn{padding:9px 20px;font-size:15px}

.hero{height:440px;background:linear-gradient(100deg,var(--green-1) 0%,#1f7d34 35%,var(--green-2) 60%,#1a5e9a 100%);position:relative;overflow:hidden}
.hero h1{font-family:"Oswald",sans-serif;font-weight:400;color:var(--white);font-size:46px;line-height:1.2;text-transform:uppercase;width:700px;padding-top:58px}
.hero .btn{font-family:"Oswald",sans-serif;font-weight:400;font-size:28px;padding:8px 30px;margin-top:30px;background:var(--white);color:var(--green-1);text-transform:uppercase}
.hero-photo{position:absolute;right:60px;top:20px;width:360px;height:420px;background:linear-gradient(180deg,#5a6470,#262c33);border-radius:160px 160px 0 0}

.finder{height:900px;padding-top:50px;overflow:hidden}
.finder-top{display:flex;justify-content:space-between}
.finder-text{width:520px}
.finder h2{font-family:"Oswald",sans-serif;font-weight:400;font-size:32px;line-height:1.3;color:var(--blue-dark);border-bottom:3px solid var(--blue);padding-bottom:8px;margin-bottom:22px;white-space:nowrap}
.finder-text p{margin-bottom:16px}
.video-col{width:500px;padding-top:4px}
.video{height:300px;background:linear-gradient(160deg,#dfe3e6,#9aa3aa);position:relative}
.video svg{position:absolute;left:50%;top:50%;transform:translate(-50%,-50%)}
.video-col .btn{display:block;text-align:center;margin-top:22px;padding:11px;font-size:17px}

.criteria{margin:18px 0 0 20px;border-collapse:collapse}
.criteria td{padding:9px 0;white-space:nowrap}
.criteria td:first-child{color:var(--blue);width:220px}
.finder-after{margin-top:26px}
.finder-after .btn{font-family:"Oswald",sans-serif;font-weight:400;font-size:24px;padding:8px 30px;margin-top:30px;text-transform:uppercase}

.notes{height:420px;background:var(--note-bg);padding-top:42px;overflow:hidden}
.notes h2{font-family:"Oswald",sans-serif;font-weight:400;font-size:36px;color:var(--blue-dark);border-bottom:3px solid var(--blue);display:inline-block;padding-bottom:2px;margin-bottom:26px}
.notes li{list-style:none;display:flex;gap:16px;margin-bottom:18px;padding-bottom:16px;border-bottom:1px solid var(--line)}
.notes li svg{flex:none;margin-top:2px}

.site-footer{height:220px;background:var(--foot-bg);padding-top:40px}
.site-footer .wrap{display:flex;gap:50px}
.foot-col{flex:1}
.foot-col h3{font-family:"Oswald",sans-serif;font-weight:400;font-size:26px;color:var(--blue-dark);border-bottom:3px solid var(--blue);padding-bottom:6px;margin-bottom:22px}
.foot-col .btn{padding:11px 20px;font-size:17px;display:flex;justify-content:space-between;align-items:center}
.phone{font-family:"Oswald",sans-serif;font-size:38px;color:#333;display:flex;align-items:center;gap:12px;line-height:1}
.email{font-size:18px;color:#333;display:flex;align-items:center;gap:12px}
.copyright{height:76px;line-height:76px;background:var(--white);text-align:center;font-size:14px;color:var(--muted);border-top:1px solid var(--line)}
.copyright strong{color:var(--blue)}
</style>
</head>
<body>
<header class="site-header">
  <div class="wrap">
    <div class="brand">Free Industry Services</div>
    <div class="header-contact">
      <span><svg width="18" height="18" viewBox="0 0 24 24"><path fill="#fff" d="M6.6 10.8a15.1 15.1 0 0 0 6.6 6.6l2.2-2.2c.3-.3.7-.4 1-.2 1.1.4 2.3.6 3.6.6.6 0 1 .4 1 1V20c0 .6-.4 1-1 1A17 17 0 0 1 3 4c0-.6.4-1 1-1h3.5c.6 0 1 .4 1 1 0 1.3.2 2.5.6 3.6.1.3 0 .7-.2 1z"/></svg>1300 42 71 65</span>
      <span><svg width="20" height="15" viewBox="0 0 22 16"><rect x="1" y="1" width="20" height="14" fill="none" stroke="#fff" stroke-width="2"/><path d="M1 1l10 8 10-8" fill="none" stroke="#fff" stroke-width="2"/></svg>suggestions@podiumvoicehub.com.au</span>
      <a class="btn" href="#">Contact Form</a>
    </div>
  </div>
</header>

<section class="hero">
  <div class="hero-photo" role="img" aria-label="Photograph of a business speaker in a dark suit"></div>
  <div class="wrap">
    <h1>Are you looking for a guest or keynote speaker - inspiring, entertaining, industry expert etc, for a conference or special event?</h1>
    <a class="btn" href="#">Contact Us Now!</a>
  </div>
</section>

<section class="finder">
  <div class="wrap">
    <div class="finder-top">
      <div class="finder-text">
        <h2>Find the Speaker for Your Next Event</h2>
        <p>Podium Voice Hub is a free industry service designed to help people looking for speakers save precious time and frustration in finding the most suitable/best speaker for their needs.</p>
        <p>Suggestions are given by Australian conference speaker Glen Tarrant who has presented around Australia for a number of years and is familiar with many of our top professional speakers, MC's as well as the leading speaker bureaus.</p>
        <p>If you would like a hand finding good speaker options, simply send us the details of your event and the type of presenter you are ideally after, e.g.</p>
      </div>
      <div class="video-col">
        <div class="video" role="img" aria-label="Video still of the presenter speaking to camera">
          <svg width="64" height="64" viewBox="0 0 64 64"><circle cx="32" cy="32" r="30" fill="none" stroke="#fff" stroke-width="3"/><path d="M26 20l18 12-18 12z" fill="#fff"/></svg>
        </div>
        <a class="btn" href="#">I Want to Make our Event a Great Success</a>
      </div>
    </div>
    <table class="criteria">
      <tr><td>Type/Style</td><td>Motivational, Entertaining, Keynote/Workshop, MC etc</td></tr>
      <tr><td>Topic/Area</td><td>Team Building, Leadership, Inspiration, Health/Life Balance etc</td></tr>
      <tr><td>Approximate Budget</td><td>$1000, $1500, $3000, $7000+ etc</td></tr>
      <tr><td>Location</td><td>Sydney, Melbourne, Brisbane, Perth, Adelaide, Canberra etc</td></tr>
    </table>
    <div class="finder-after">
      <p>and where we can, we will be happy to send you some speaker possibilities/ideas, trusted speakers bureaus or simply some thoughts on the best places for you to look. Regards GT</p>
      <a class="btn" href="#">Enquiry Now!</a>
    </div>
  </div>
</section>

<section class="notes">
  <div class="wrap">
    <h2>Please Note:</h2>
    <ul>
      <li><svg width="20" height="20" viewBox="0 0 22 22"><circle cx="11" cy="11" r="11" fill="var(--blue)"/><path d="M6 11l3.5 3.5L16 8" fill="none" stroke="#fff" stroke-width="2.4"/></svg>Any information you provide will ONLY ever be used to help with your specific enquiry.</li>
      <li><svg width="20" height="20" viewBox="0 0 22 22"><circle cx="11" cy="11" r="11" fill="var(--blue)"/><path d="M6 11l3.5 3.5L16 8" fill="none" stroke="#fff" stroke-width="2.4"/></svg>Glen does not have any financial agreements with any individual speakers he recommends. He offers this service, as it only takes a few minutes of his time, helps promote other professional speakers and obviously keeps his own name out there in the industry.</li>
      <li><svg width="20" height="20" viewBox="0 0 22 22"><circle cx="11" cy="11" r="11" fill="var(--blue)"/><path d="M6 11l3.5 3.5L16 8" fill="none" stroke="#fff" stroke-width="2.4"/></svg>Please understand that while Glen tries to respond quickly, due to his own speaking/travel commitments it may take up to 24 hours.</li>
    </ul>
  </div>
</section>

<footer>
  <div class="site-footer">
    <div class="wrap">
      <div class="foot-col">
        <h3>Please Submit</h3>
        <a class="btn" href="#">Quick Online Contact Form <svg width="12" height="16" viewBox="0 0 14 18"><path d="M2 1l10 8-10 8z" fill="#fff"/></svg></a>
      </div>
      <div class="foot-col">
        <h3>Quick Contact No.</h3>
        <div class="phone"><svg width="28" height="28" viewBox="0 0 24 24"><path fill="#333" d="M6.6 10.8a15.1 15.1 0 0 0 6.6 6.6l2.2-2.2c.3-.3.7-.4 1-.2 1.1.4 2.3.6 3.6.6.6 0 1 .4 1 1V20c0 .6-.4 1-1 1A17 17 0 0 1 3 4c0-.6.4-1 1-1h3.5c.6 0 1 .4 1 1 0 1.3.2 2.5.6 3.6.1.3 0 .7-.2 1z"/></svg>123 456 7890</div>
      </div>
      <div class="foot-col">
        <h3>Get In Touch Email</h3>
        <div class="email"><svg width="24" height="17" viewBox="0 0 22 16"><rect x="1" y="1" width="20" height="14" fill="none" stroke="#333" stroke-width="2"/><path d="M1 1l10 8 10-8" fill="none" stroke="#333" stroke-width="2"/></svg>info@podiumvoicehub.com.au</div>
      </div>
    </div>
  </div>
  <div class="copyright">© <strong>SPEAKER NAME</strong> - 2015. All Rights Reserved.</div>
</footer>
</body>
</html>
```